Therapy Dog Organization Website

Looking for a website that is user friendly, welcoming, dog themed and has the following pages and links:
*Click here to join - links to a jot form
*Click here to donate - links to our paypal page
*Request a visit - links to a jot form
*social link Follow Link
*social link Follow Link
*Our team - images uploaded to showcase our dogs
*Donors and Referrals Page - Where I can update as donations and referrals come in.
*Online store. Currently this is in Jot Form but I would like a store front. I would not want this to be a link but rather a hidden page, something like www.brightmeadow.org/teamstore.

Please visit www.brightmeadow.org to see what we have right now designed simply in Canva. Dog photos can be provided to use in images.

Note: I have funds from a grant that I have to spend to add gratuity to the project winner.

```html
<!DOCTYPE html>
<html lang="en">
<head>
<meta charset="utf-8">
<title>Bright Meadow Therapy Dogs</title>
<link href="https://fonts.googleapis.com/css2?family=Anton&family=Outfit:wght@400;500;600;700&family=Lilita+One&display=swap" rel="stylesheet">
<style>
:root{
  --teal:#4fd8dd;
  --teal-deep:#33c2c8;
  --ink:#141414;
  --white:#ffffff;
  --grey:#e7e7e7;
  --grey-text:#dcdcdc;
  --footer:#0e0e0e;
  --social-a:#2f6fe0;
  --social-b:#d9428a;
}
*{box-sizing:border-box;margin:0;padding:0}
html,body{width:1200px;height:4605px;overflow:hidden}
body{font-family:"Outfit",sans-serif;color:var(--ink);background:var(--white);position:relative}
.display{font-family:"Anton",sans-serif;font-weight:400;text-transform:uppercase;line-height:1}
section,header,footer{position:absolute;left:0;width:1200px}
.abs{position:absolute}
.btn{display:inline-flex;align-items:center;gap:8px;height:34px;padding:0 18px;border-radius:17px;font-size:13px;font-weight:500;color:var(--ink);text-decoration:none;white-space:nowrap}
.btn-white{background:var(--white)}
.btn-teal{background:var(--teal)}
.btn svg{width:14px;height:14px}
.photo{border-radius:18px}
/* header */
.site-header{top:0;height:56px;background:var(--teal)}
.nav a{position:absolute;top:20px;font-size:13px;color:var(--ink);text-decoration:none;font-weight:500}
.brand-bubble{position:absolute;left:540px;top:-40px;width:120px;height:128px;border-radius:50%;background:var(--teal)}
.brand{position:absolute;left:540px;top:18px;width:120px;text-align:center;color:var(--white);font-weight:700;font-size:15px;line-height:1.05}
.brand small{display:block;font-size:9px;font-weight:700;letter-spacing:1px}
.social{position:absolute;top:14px;width:28px;height:28px;border-radius:50%;border:3px solid var(--white)}
.social.one{background:var(--social-a)}
.social.two{background:var(--social-b)}
/* hero */
.hero{top:56px;height:516px}
.hero .photo{position:absolute;inset:0;border-radius:0;background:linear-gradient(90deg,#5e5149 0%,#8d7868 45%,#c7b3a0 75%,#e0d4c6 100%)}
.hero-copy{position:absolute;left:196px;top:76px;width:344px;text-align:center;color:var(--white)}
.hero-copy h1{font-size:50px;letter-spacing:1px;line-height:1.05}
.hero-copy h1 .t{color:var(--teal)}
.hero-copy h1 .sm{font-size:36px}
.hero-copy p{font-size:11px;line-height:1.6;margin-top:18px}
.hero-copy .ctas{margin-top:18px;display:flex;gap:6px;justify-content:center}
/* story */
.story{top:572px;height:510px;background:var(--teal)}
.story .frame{left:186px;top:50px;width:430px;height:370px;background:var(--white);border-radius:16px;transform:rotate(-4deg)}
.story .photo{left:210px;top:76px;width:392px;height:356px;background:linear-gradient(135deg,#3a3a3a,#6d5a4e 50%,#2a5d8a)}
.story .copy{left:648px;top:105px;width:320px}
.story h2{font-size:44px}
.story p{font-size:11.5px;line-height:1.6;margin-top:16px}
/* mission */
.mission{top:1082px;height:559px}
.mission .ghost{left:318px;top:20px;font-size:160px;color:var(--grey-text);letter-spacing:4px}
.mission .block{left:765px;top:44px;width:258px;height:462px;background:var(--teal);border-radius:14px}
.mission .photo{left:563px;top:86px;width:406px;height:380px;background:linear-gradient(150deg,#1d3b66,#b58a5a 45%,#6b4a2f)}
.mission .copy{left:241px;top:148px;width:290px}
.mission h2{font-size:46px;line-height:1.08;color:var(--ink)}
.mission p{font-size:11.5px;line-height:1.65;margin-top:26px}
/* purpose */
.purpose{top:1641px;height:478px}
.purpose .photo{position:absolute;inset:0;border-radius:0;background:linear-gradient(90deg,#b6b0a6 0%,#8b8175 35%,#5a5650 60%,#3c3c3c 100%)}
.purpose .copy{left:692px;top:82px;width:300px;color:var(--white)}
.purpose h2{font-size:54px;line-height:1.02}
.purpose h2 .t{color:var(--teal)}
.purpose p{font-size:11.5px;line-height:1.65;margin-top:14px}
/* team */
.team{top:2119px;height:595px}
.section-title{width:100%;text-align:center;font-size:50px}
.team .section-title{top:88px}
.team .cards{left:182px;top:170px;display:flex;gap:10px}
.dog-card{width:202px;height:286px;border-radius:8px;background:#a6e8b5;padding:6px;position:relative}
.dog-card .inner{width:100%;height:100%;border-radius:6px;background:#5a86d6;position:relative;overflow:hidden}
.dog-card h3{font-family:"Lilita One",sans-serif;color:var(--white);font-size:28px;text-align:center;font-weight:400;margin-top:4px}
.dog-card .pic{position:absolute;left:6px;right:6px;top:44px;height:190px;background:linear-gradient(180deg,#8b7d70,#cfc7c0)}
.dog-card .tag{position:absolute;left:0;right:0;bottom:10px;text-align:center;color:var(--white);font-weight:700;font-size:15px}
.arrow{position:absolute;width:40px;height:40px;border-radius:50%;background:var(--teal);top:293px}
.arrow svg{width:40px;height:40px}
.team .more{left:504px;top:500px}
/* store */
.store{top:2714px;height:567px;background:var(--grey)}
.store .section-title{top:68px}
.store .sub{top:126px;width:100%;text-align:center;font-size:12px}
.store .items{left:178px;top:155px;display:flex;gap:10px}
.item{width:204px}
.item .box{height:232px;background:var(--white);border-radius:20px;display:flex;align-items:center;justify-content:center}
.item .prod{width:150px;height:150px;border-radius:20px}
.item h4{font-family:"Anton",sans-serif;font-weight:400;text-transform:uppercase;text-align:center;font-size:15px;margin-top:14px}
.store .visit{left:525px;top:478px}
/* donors */
.donors{top:3281px;height:520px}
.donors .title{left:260px;top:48px;width:300px;text-align:center}
.donors .title .l1{font-size:50px;display:block}
.donors .title .l2{font-size:50px;display:inline-block;background:var(--teal);padding:2px 14px 6px;border-radius:12px;margin-top:2px}
.donors .copy{left:190px;top:178px;width:450px;text-align:center;font-size:11.5px;line-height:1.6}
.donors .copy p+p{margin-top:14px}
.donors .view{left:310px;top:388px}
.donors .ring{left:670px;top:55px;width:322px;height:322px;border-radius:50%;background:#ededed}
.donors .photo{left:690px;top:40px;width:290px;height:345px;border-radius:0 0 145px 145px;background:linear-gradient(180deg,#d9d2c8,#8a6a4a 55%,#2b2b2b)}
.donors .swirl{left:620px;top:330px}
/* contact */
.contact-ghost{top:3810px;height:110px;font-size:140px;color:var(--grey-text);text-align:center;letter-spacing:4px}
.contact{top:3912px;height:361px;background:var(--teal-deep)}
.contact .photo{left:179px;top:-184px;width:509px;height:545px;border-radius:0;background:linear-gradient(180deg,#9a7e68,#d98aa9 60%,#c2568a)}
.contact .copy{left:690px;top:70px;width:310px;text-align:center;color:var(--white)}
.contact h2{font-size:54px;line-height:1.02}
.contact .btn{margin-top:20px}
/* footer */
.site-footer{top:4273px;height:332px;background:var(--footer);color:var(--white)}
.site-footer .brand-f{left:170px;top:85px;font-weight:700;font-size:28px;line-height:1}
.site-footer .brand-f small{display:block;font-size:13px;font-weight:700;letter-spacing:2px;margin-top:4px}
.col{top:80px}
.col h5{font-family:"Anton",sans-serif;font-weight:400;text-transform:uppercase;font-size:19px;margin-bottom:14px}
.col a,.col span{display:block;font-size:12px;color:var(--white);text-decoration:none;margin-bottom:12px}
.col .row{display:flex;gap:8px;align-items:flex-start}
.col .row svg{width:13px;height:13px;flex:none;margin-top:2px}
.col .socials{display:flex;gap:6px;margin-top:4px}
.col .socials i{width:30px;height:30px;border-radius:50%;display:block}
.site-footer .rule{left:150px;top:290px;width:900px;height:1px;background:#333}
.site-footer .copy{top:305px;width:100%;text-align:center;font-size:11px;color:#cfcfcf}
</style>
</head>
<body>

<header class="site-header">
  <nav class="nav">
    <a href="#" style="left:172px">Home</a>
    <a href="#" style="left:236px">Our Story</a>
    <a href="#" style="left:318px">Mission &amp; Purpose</a>
    <a href="#" style="left:450px">Our Team</a>
    <a href="#" style="left:676px">Donors and Referrals</a>
  </nav>
  <div class="brand-bubble"></div>
  <div class="brand">Bright Meadow<small>Therapy Dogs</small></div>
  <a class="btn btn-white abs" href="#" style="left:833px;top:11px">Click here to join</a>
  <span class="social one" style="left:974px"></span>
  <span class="social two" style="left:1008px"></span>
</header>

<section class="hero">
  <div class="photo" role="img" aria-label="Photo of a young boy hugging a husky puppy on a rug"></div>
  <div class="hero-copy">
    <h1 class="display">Bringing<br><span class="t">Comfort</span>, Joy<br>and<br><span class="t sm">Unconditional</span><br><span class="sm">Love – One Paw at<br>a Time.</span></h1>
    <p>A Michigan Nonprofit dedicated to providing Therapy Dogs<br>to the community to spread joy, hope and healing.</p>
    <div class="ctas">
      <a class="btn btn-white" href="#">Click here to donate <svg viewBox="0 0 20 20"><circle cx="10" cy="13" r="4"/><circle cx="4" cy="8" r="2"/><circle cx="8" cy="4" r="2"/><circle cx="12" cy="4" r="2"/><circle cx="16" cy="8" r="2"/></svg></a>
      <a class="btn btn-teal" href="#">Request a visit <svg viewBox="0 0 20 20"><circle cx="10" cy="13" r="4"/><circle cx="4" cy="8" r="2"/><circle cx="8" cy="4" r="2"/><circle cx="12" cy="4" r="2"/><circle cx="16" cy="8" r="2"/></svg></a>
    </div>
  </div>
</section>

<section class="story">
  <svg class="abs" style="left:592px;top:20px" width="16" height="36" viewBox="0 0 16 36"><rect x="2" y="2" width="12" height="22" rx="6" fill="none" stroke="#141414" stroke-width="1.6"/><line x1="8" y1="7" x2="8" y2="12" stroke="#141414" stroke-width="1.6"/><line x1="8" y1="28" x2="8" y2="34" stroke="#141414" stroke-width="1.6"/></svg>
  <div class="abs frame"></div>
  <div class="abs photo" role="img" aria-label="Photo of a therapy dog in a blue vest resting on a visitor's lap"></div>
  <div class="abs copy">
    <h2 class="display">Our Story</h2>
    <p>Every wag tells a story – and ours began with a simple belief: the love of a dog can change lives.</p>
    <p>What started with a few volunteers and their dogs has grown into a community dedicated to bringing comfort and joy wherever it's needed most. From hospitals to schools and senior centers, our therapy dog teams share moments of connection, calm, and healing – one visit at a time.</p>
    <p>At the heart of our mission is a simple truth – sometimes the best kind of therapy comes with four paws and a wagging tail.</p>
  </div>
</section>

<section class="mission">
  <div class="abs ghost display">Mission</div>
  <div class="abs block"></div>
  <div class="abs photo" role="img" aria-label="Photo of a smiling therapy dog wearing a bandana and vest"></div>
  <div class="abs copy">
    <h2 class="display">Our<br>Mission</h2>
    <p>To certify, and deploy therapy dog teams that promote emotional well-being, reduce stress, and foster empathy. We are dedicated to improving quality of life by bringing the unconditional love and calming presence of therapy dogs to those in need, while upholding the highest standards of animal welfare, professionalism, and community service</p>
  </div>
</section>

<section class="purpose">
  <div class="photo" role="img" aria-label="Photo of a boy petting a therapy dog in a playroom"></div>
  <div class="abs copy">
    <h2 class="display">Our<br><span class="t">Purpose</span></h2>
    <p>Our purpose is to share the comfort, joy, and healing power of the human animal bond. We connect trained therapy dog teams with people in need of emotional support, companionship, and encouragement in hospitals, schools, senior communities, and beyond.</p>
    <p style="margin-top:12px">Through every visit, we aim to lift spirits, ease stress, and remind people that kindness and connection can come on four paws and a wagging tail.</p>
  </div>
</section>

<section class="team">
  <h2 class="abs section-title display">Our Team</h2>
  <span class="arrow" style="left:152px"><svg viewBox="0 0 40 40"><path d="M23 13l-7 7 7 7" fill="none" stroke="#fff" stroke-width="3" stroke-linecap="round"/></svg></span>
  <span class="arrow" style="left:1011px"><svg viewBox="0 0 40 40"><path d="M17 13l7 7-7 7" fill="none" stroke="#fff" stroke-width="3" stroke-linecap="round"/></svg></span>
  <div class="abs cards">
    <div class="dog-card"><div class="inner"><h3>Ash</h3><div class="pic" role="img" aria-label="Photo of Ash, a husky in a pink bandana"></div><div class="tag">Bright Meadow</div></div></div>
    <div class="dog-card"><div class="inner"><h3>Mira</h3><div class="pic" role="img" aria-label="Photo of Mira, a husky in a pink bandana"></div><div class="tag">Bright Meadow</div></div></div>
    <div class="dog-card"><div class="inner"><h3>Wren</h3><div class="pic" role="img" aria-label="Photo of Wren, a merle dog in a pink bandana"></div><div class="tag">Bright Meadow</div></div></div>
    <div class="dog-card"><div class="inner"><h3>Bramble</h3><div class="pic" role="img" aria-label="Photo of Bramble, a golden retriever" style="background:linear-gradient(180deg,#7a6a5a,#d6a25a)"></div><div class="tag">Bright Meadow</div></div></div>
  </div>
  <a class="btn btn-teal abs more" href="#">Meet The Whole Pack <svg viewBox="0 0 20 20"><circle cx="10" cy="13" r="4"/><circle cx="4" cy="8" r="2"/><circle cx="8" cy="4" r="2"/><circle cx="12" cy="4" r="2"/><circle cx="16" cy="8" r="2"/></svg></a>
</section>

<section class="store">
  <h2 class="abs section-title display">Online Store</h2>
  <p class="abs sub">Shop our exclusive Bright Meadow gear and help support our pups!</p>
  <div class="abs items">
    <div class="item"><div class="box"><div class="prod" role="img" aria-label="Navy hoodie product photo" style="background:#1c2b4a"></div></div><h4>Hoodies</h4></div>
    <div class="item"><div class="box"><div class="prod" role="img" aria-label="Grey t-shirt product photo" style="background:#8c8c8c"></div></div><h4>T-Shirt</h4></div>
    <div class="item"><div class="box"><div class="prod" role="img" aria-label="White mug product photo" style="background:linear-gradient(135deg,#f4f4f4,#cfd6e6)"></div></div><h4>Mug</h4></div>
    <div class="item"><div class="box"><div class="prod" role="img" aria-label="Navy cap product photo" style="background:#1a2748"></div></div><h4>Cap</h4></div>
  </div>
  <a class="btn btn-teal abs visit" href="#">Visit Our Store <svg viewBox="0 0 20 20"><circle cx="10" cy="13" r="4"/><circle cx="4" cy="8" r="2"/><circle cx="8" cy="4" r="2"/><circle cx="12" cy="4" r="2"/><circle cx="16" cy="8" r="2"/></svg></a>
</section>

<section class="donors">
  <h2 class="abs title display"><span class="l1">Donors &amp;</span><span class="l2">Referrals</span></h2>
  <div class="abs copy">
    <p>Our donors and referral partners are the heart of our organization. Because of their generosity, we are able to keep costs low for our therapy dog teams while never compromising the integrity, training, and care of our handlers and dogs.</p>
    <p>Every visit, every wagging tail, and every moment of comfort is made possible by your kindness, our dedicated volunteers, and a whole lot of furry friends and helping paws.</p>
    <p>Thank you for believing in our mission and helping us spread healing one paw at a time.</p>
  </div>
  <a class="btn btn-teal abs view" href="#">View Donors &amp; Referrals <svg viewBox="0 0 20 20"><circle cx="10" cy="13" r="4"/><circle cx="4" cy="8" r="2"/><circle cx="8" cy="4" r="2"/><circle cx="12" cy="4" r="2"/><circle cx="16" cy="8" r="2"/></svg></a>
  <div class="abs ring"></div>
  <div class="abs photo" role="img" aria-label="Photo of two therapy dogs in matching bandanas"></div>
  <svg class="abs swirl" width="420" height="80" viewBox="0 0 420 80"><path d="M10 60 C80 10 140 20 190 50 S300 80 330 30 S390 10 410 20" fill="none" stroke="#33c2c8" stroke-width="2"/></svg>
</section>

<div class="abs contact-ghost display" style="left:0;width:1200px">Contact Us</div>
<section class="contact">
  <div class="abs photo" role="img" aria-label="Photo of a smiling girl holding two therapy dogs"></div>
  <div class="abs copy">
    <h2 class="display">Please Click<br>Here to<br>Contact Us</h2>
    <a class="btn btn-white" href="#">Please Click Here to Contact Us <svg viewBox="0 0 20 20"><circle cx="10" cy="13" r="4"/><circle cx="4" cy="8" r="2"/><circle cx="8" cy="4" r="2"/><circle cx="12" cy="4" r="2"/><circle cx="16" cy="8" r="2"/></svg></a>
  </div>
</section>

<footer class="site-footer">
  <div class="abs brand-f">Bright Meadow<small>Therapy Dogs</small></div>
  <div class="abs col" style="left:404px">
    <h5>Quick Links</h5>
    <a href="#">Home</a><a href="#">Our Story</a><a href="#">Mission &amp; Purpose</a><a href="#">Our Team</a><a href="#">Donors and Referrals</a>
  </div>
  <div class="abs col" style="left:619px">
    <h5>Get Involed</h5>
    <a href="#">Click Here to Join</a><a href="#">Click Here to Donate</a><a href="#">Request a Visit</a>
    <div class="socials"><i style="background:var(--social-a)"></i><i style="background:var(--social-b)"></i></div>
  </div>
  <div class="abs col" style="left:833px;width:180px">
    <h5>Contact Us</h5>
    <span class="row"><svg viewBox="0 0 16 16"><rect x="1" y="3" width="14" height="10" rx="1" fill="none" stroke="#fff" stroke-width="1.4"/><path d="M1 4l7 5 7-5" fill="none" stroke="#fff" stroke-width="1.4"/></svg>info@brightmeadow.org</span>
    <span class="row"><svg viewBox="0 0 16 16"><path d="M4 1l3 3-2 2c1 2 3 4 5 5l2-2 3 3-2 3C7 15 1 9 1 3z" fill="#fff"/></svg>(555) 014-2290</span>
    <span class="row"><svg viewBox="0 0 16 16"><path d="M8 1a5 5 0 0 1 5 5c0 4-5 9-5 9S3 10 3 6a5 5 0 0 1 5-5z" fill="#fff"/><circle cx="8" cy="6" r="2" fill="#0e0e0e"/></svg>Serving our community<br>with love</span>
  </div>
  <div class="abs rule"></div>
  <p class="abs copy">Copyright © 2026 Bright Meadow. All rights reserved.</p>
</footer>

</body>
</html>
```